11月下旬に国立大学にて講演会をすることになりました。
その際のチラシのデザインの作成をお願いしたいです。

入れる内容は決まっておりますので、デザインを作っていただきたいです。

■チラシの使用用途
告知(データベースがメイン)
メルマガで流す
ホームページ掲載

今の所、こちらを検討しておりますので
それによってサイズを合わせていただければと思います。

ご不明点・ご質問などございましたら、お問い合わせください。
添付資料のWordデータをご確認ください。
基本はA4かA3で検討しておりますが、どちらのサイズでもできるようにして欲しいです。
片面
青系、水色系、配色は、健康系なのでシックだけど明るい感じがいいです
• 高解像度JPG (.jpg)
• イラストレーター形式 (.ai)
• PNG形式 (.png)
【追加依頼】です。

大学の教授の部分ですが、
少し自己紹介を追加することになりました。

180-200文字程度の情報を追加していただきたいので、
そこの部分の空間の確保をお願いします。
チラシの作成していただきまして、あ理がとうございます。

先方に確認をとりまして、作成していただいたチラシに
以下の情報を追加して作成していただけますでしょうか?

---------------------------------------
高森 悠介
国立大学法人翠峰大学環境共生学部
ウェルネス研究分野 教授 医学博士
ハーウッド大学客員教授
全米ビジネス書ベストセラー『The Quiet Harbor(クワイエットハーバー) 2nd edition世界の100 歳人に学ぶ健康と長寿9つのルール』(2022年、緑陽舎)翻訳・監修者。
ウェルネス研究、ウェルネスツーリズム研究の第一人者。海洋療法学者。

よろしくお願いします。

国立大学での講義という点で清潔感があり、スタイリッシュなデザインから見やすさ、分かりやすさなどからこちらのデザインにさせていただきました。

たくさんの方にご応募・ご協力いただきまして、ありがとうございました。

```html
<!DOCTYPE html>
<html lang="ja">
<head>
<meta charset="utf-8">
<title>腰痛テンプレート施術 公開講座</title>
<link rel="stylesheet" href="https://fonts.googleapis.com/css2?family=Noto+Sans+JP:wght@400;500;700;900&family=Roboto+Condensed:wght@500;700&display=swap">
<style>
:root{
  --main:#4fb6e6;
  --blue:#1f86c8;
  --navy:#0f4f7d;
  --ink:#1a1a1a;
  --grey:#6d7780;
  --pale:#eaf6fc;
  --paper:#ffffff;
}
*{margin:0;padding:0;box-sizing:border-box}
html,body{width:846px;height:1200px;overflow:hidden;background:var(--paper)}
body{font-family:"Noto Sans JP",sans-serif;color:var(--ink);position:relative}
.header{position:absolute;top:18px;left:40px;right:40px;height:70px;display:flex;justify-content:space-between;align-items:flex-start}
.org{display:flex;flex-direction:column;gap:4px}
.org-name{display:flex;align-items:center;gap:8px;font-weight:700;font-size:19px}
.org-name .mark{width:16px;height:16px;background:var(--ink)}
.org-sub{font-size:9px;color:#333}
.cohost{position:absolute;left:50%;top:0;transform:translateX(-50%)}
.cohost .x{font-size:44px;line-height:44px;font-weight:300;color:var(--ink)}
.org.right .org-name{font-size:16px;letter-spacing:.5px}
.org.right .mark{border-radius:50%}
.title-band{position:absolute;top:98px;left:40px;width:766px;height:78px;background:var(--main);display:flex;align-items:center;justify-content:center}
.title-band h1{font-size:58px;font-weight:900;letter-spacing:2px;color:var(--ink)}
.sub-row{position:absolute;top:184px;left:40px;right:40px;height:66px;display:flex;align-items:center}
.sub-title{background:var(--main);height:66px;padding:0 18px;display:flex;align-items:center;font-size:46px;font-weight:900;color:var(--ink)}
.date{margin-left:18px;font-family:"Roboto Condensed",sans-serif}
.date .day{font-size:38px;font-weight:700;line-height:38px}
.date .day small{font-size:18px;font-family:"Noto Sans JP",sans-serif}
.date .time{font-size:22px;font-weight:700}
.fee{margin-left:22px;display:flex;align-items:center;gap:6px}
.fee .label{writing-mode:vertical-rl;font-size:12px;font-weight:700}
.fee .free{font-size:40px;font-weight:900}
.fee .note{font-size:8px;color:var(--grey);width:90px;line-height:1.5}
.intro{position:absolute;top:266px;left:40px;width:766px;font-size:12px;line-height:1.8;color:var(--navy);font-weight:500;text-align:justify}
.photo{position:absolute;top:382px;left:40px;width:766px;height:226px;background:linear-gradient(135deg,#0f4f7d,#3c9fd6 55%,#155d8e)}
.venue{position:absolute;top:624px;left:40px;display:flex;align-items:center;gap:10px}
.badge{width:40px;height:40px;border-radius:50%;background:var(--blue);color:#fff;font-size:12px;font-weight:700;display:flex;align-items:center;justify-content:center}
.venue .text{font-size:21px;font-weight:700}
.capacity{position:absolute;top:672px;left:40px;display:flex;align-items:center;gap:10px}
.capacity .text{font-size:32px;font-weight:900}
.capacity .text small{font-size:10px;font-weight:400;color:var(--grey)}
.rule{position:absolute;top:732px;left:40px;right:40px;height:2px;background:var(--blue)}
.person{position:absolute;top:748px;width:370px}
.person.left{left:40px}
.person.right{left:436px}
.person .role{font-size:13px;font-weight:700;color:var(--blue);border-bottom:1px solid var(--blue);padding-bottom:5px;margin-bottom:14px}
.person .head{display:flex;gap:14px;align-items:flex-start}
.portrait{width:92px;height:92px;border-radius:50%;background:linear-gradient(#dcecf6,#9cc9e6);flex:none}
.person .name{font-size:20px;font-weight:700}
.person .name small{font-size:10px;font-weight:400;color:var(--grey)}
.person .title{font-size:11px;line-height:1.65;margin-top:6px}
.person .bio{font-size:11px;line-height:1.9;margin-top:16px;text-align:justify;color:#333}
.footer{position:absolute;bottom:26px;left:40px;right:40px;height:44px;background:var(--pale);border-left:6px solid var(--blue);display:flex;align-items:center;padding-left:16px;font-size:14px;font-weight:500}
.footer .label{color:var(--blue);margin-right:14px;font-weight:700}
</style>
</head>
<body>
<header class="header">
  <div class="org">
    <div class="org-name"><span class="mark"></span>Care Script Press</div>
    <div class="org-sub">株式会社ケアスクリプト</div>
  </div>
  <div class="cohost"><div class="x">×</div></div>
  <div class="org right">
    <div class="org-name"><span class="mark"></span>SUIHO UNIVERSITY</div>
    <div class="org-sub">翠峰大学環境共生学部ウェルネス研究分野</div>
  </div>
</header>

<div class="title-band"><h1>腰痛テンプレート施術</h1></div>
<div class="sub-row">
  <div class="sub-title">公開講座</div>
  <div class="date">
    <div class="day">11/23<small>(祝)</small></div>
    <div class="time">10:30–17:00</div>
  </div>
  <div class="fee">
    <span class="label">受講料</span>
    <span class="free">無料</span>
    <span class="note">※事前お申し込みが必要です。定員に達し次第締切。</span>
  </div>
</div>

<p class="intro">国民病ともいわれる腰痛は、多くの人の日常生活に大きな影響を与えています。本講座では、施術の現場で実践されている「腰痛テンプレート施術」を、基礎理論から具体的な手技まで分かりやすく解説します。医療・健康分野に携わる方はもちろん、ご自身の体を整えたい一般の方にもご参加いただける内容です。大学の研究成果と現場の知見を結びつけ、明日から役立つ実践的な視点をお届けします。健康と長寿を支えるウェルネスの考え方にも触れながら、体と向き合うための新しいヒントを学ぶ一日です。</p>

<div class="photo" role="img" aria-label="講義室で受講する多くの参加者の様子(写真)"></div>

<div class="venue"><span class="badge">会場</span><span class="text">国立大学法人 翠峰大学 文系講義棟215教室</span></div>
<div class="capacity"><span class="badge">定員</span><span class="text">100名 先着順 <small>※定員に達し次第締切</small></span></div>
<div class="rule"></div>

<section class="person left">
  <div class="role">講師プロフィール</div>
  <div class="head">
    <div class="portrait" role="img" aria-label="講師の顔写真"></div>
    <div>
      <div class="name">野村 航平 <small>(のむら こうへい)</small></div>
      <div class="title">理学療法士、柔道整復師<br>株式会社ケアスクリプト 代表取締役</div>
    </div>
  </div>
  <p class="bio">臨床現場で長年にわたり腰痛に悩む患者の施術に携わる。独自に体系化した「腰痛テンプレート施術」は再現性の高さから多くの治療家に支持されている。全国で講習会を開催し、後進の育成にも力を注ぐ。専門誌への寄稿や書籍の執筆のほか、医療機関や企業との共同研究にも参画し、科学的根拠に基づく施術の普及に取り組んでいる。</p>
</section>

<section class="person right">
  <div class="role">ファシリテーター</div>
  <div class="head">
    <div class="portrait" role="img" aria-label="ファシリテーターの顔写真"></div>
    <div>
      <div class="name">高森 悠介 <small>(たかもり ゆうすけ)</small></div>
      <div class="title">国立大学法人翠峰大学環境共生学部<br>ウェルネス研究分野 教授 医学博士<br>ハーウッド大学客員教授</div>
    </div>
  </div>
  <p class="bio">全米ビジネス書ベストセラー『The Quiet Harbor(クワイエットハーバー) 2nd edition 森に暮らす人々が教える心と体を整える7つの習慣』(2022年、緑陽舎)翻訳・監修者。ウェルネス研究、ウェルネスツーリズム研究の第一人者。海洋療法学者。</p>
</section>

<footer class="footer"><span class="label">お問い合わせ先</span>info@carescript.example</footer>
</body>
</html>
```